New business card design for Pinecrest Hollow Optometry Clinic

We need a new business card design using our existing logo (uploaded). Please do not include eyes, eye exam charts or beaches, water, sand. The logo I uploaded shows our colors of green and blue, but we are open to seeing it in black OR white. We would like to see something modern and fresh. It will need to be 2 sided. On the front we will need to be able to put a doctors name, for example-Dr Marta Kellerman and Associates. We will need to be able to change the name to other doctors names when we send for printing. The back of the card should list the following: 3817 Tarrow St, Ellwick Harbour (P)705-555-0148 (E) info@phoc.ca www.phoc.ca. "We are welcoming new patients" and a line for the appointment date and time. I have uploaded the back of a card to give an example

```html
<!DOCTYPE html>
<html lang="en">
<head>
<meta charset="utf-8">
<title>Pinecrest Hollow Optometry Clinic – Appointment Card</title>
<link rel="stylesheet" href="https://fonts.googleapis.com/css2?family=Source+Sans+3:wght@400;600&display=swap">
<style>
  :root {
    --page: #ffffff;
    --card: #f8f8f8;
    --teal-deep: #027369;
    --teal-bright: #26b5a6;
    --ink: #1a1a1a;
    --on-teal: #ffffff;
    --ring: #9a9a9a;
    --crop: #b5b5b5;
  }
  html, body {
    margin: 0;
    padding: 0;
    width: 1200px;
    height: 1200px;
    overflow: hidden;
    background: var(--page);
  }
  .canvas {
    display: block;
    width: 1200px;
    height: 1200px;
    font-family: "Source Sans 3", "Source Sans Pro", sans-serif;
  }
  .card-face { fill: var(--card); }
  .panel-main { fill: var(--teal-deep); }
  .panel-accent { fill: var(--teal-bright); }
  .chevron-stripe { fill: var(--teal-deep); }
  .crop-mark { stroke: var(--crop); stroke-width: 2; }
  .practice-name { fill: var(--on-teal); font-size: 63px; font-weight: 600; }
  .title-rule { stroke: var(--on-teal); stroke-width: 3; }
  .welcome { fill: var(--on-teal); font-size: 58px; font-weight: 400; }
  .field-label { fill: var(--on-teal); font-size: 44px; font-weight: 400; }
  .field-line { stroke: var(--on-teal); stroke-width: 2; }
  .clinic-name { fill: var(--ink); font-size: 52px; font-weight: 600; }
  .contact-ring { fill: none; stroke: var(--ring); stroke-width: 1.5; }
  .contact-icon { fill: var(--teal-deep); }
  .contact-text { fill: var(--ink); font-size: 40px; font-weight: 400; }
</style>
</head>
<body>
<svg class="canvas" viewBox="0 0 1920 1920" xmlns="http://www.w3.org/2000/svg">
  <g class="crop-marks">
    <line class="crop-mark" x1="34" y1="368" x2="34" y2="390"/>
    <line class="crop-mark" x1="0" y1="402" x2="22" y2="402"/>
    <line class="crop-mark" x1="1897" y1="368" x2="1897" y2="390"/>
    <line class="crop-mark" x1="1908" y1="402" x2="1920" y2="402"/>
    <line class="crop-mark" x1="34" y1="1520" x2="34" y2="1542"/>
    <line class="crop-mark" x1="0" y1="1528" x2="22" y2="1528"/>
    <line class="crop-mark" x1="1897" y1="1520" x2="1897" y2="1542"/>
    <line class="crop-mark" x1="1908" y1="1528" x2="1920" y2="1528"/>
  </g>

  <rect class="card-face" x="48" y="402" width="1849" height="1106" rx="76"/>
  <path class="panel-accent" d="M1160,878 L1190,922 Q1214,962 1202,1008 L1053,1508 L960,1508 Z"/>
  <path class="panel-main" d="M48,478 Q48,402 124,402 L935,402 L1168,742 Q1192,775 1181,812 L968,1508 L124,1508 Q48,1508 48,1432 Z"/>
  <path class="chevron-stripe" d="M1069,402 L1092,402 L1325,742 Q1348,777 1336,815 L1133,1508 L1109,1508 L1313,815 Q1322,777 1302,742 Z"/>

  <g class="appointment">
    <text class="practice-name" x="178" y="652">Dr Marta Kellerman &amp; Associates</text>
    <line class="title-rule" x1="178" y1="671" x2="1056" y2="671"/>
    <text class="welcome" x="175" y="785">We are welcoming new patients!</text>

    <text class="field-label" x="178" y="950">Doctor:</text>
    <line class="field-line" x1="330" y1="950" x2="1071" y2="950"/>
    <text class="field-label" x="180" y="1115">Date:</text>
    <line class="field-line" x1="286" y1="1113" x2="679" y2="1113"/>
    <text class="field-label" x="172" y="1285">Time:</text>
    <line class="field-line" x1="287" y1="1283" x2="680" y2="1283"/>
  </g>

  <g class="clinic-mark">
    <text class="clinic-name" x="1600" y="660" text-anchor="middle">Pinecrest Hollow</text>
    <text class="clinic-name" x="1600" y="724" text-anchor="middle">Optometry Clinic</text>
  </g>

  <g class="contacts">
    <g class="contact-phone">
      <circle class="contact-ring" cx="1417" cy="1061" r="46"/>
      <path class="contact-icon" d="M1407,1042 Q1398,1050 1402,1062 Q1410,1075 1424,1078 Q1432,1078 1436,1072 L1428,1064 Q1424,1066 1420,1068 Q1412,1064 1410,1056 Q1412,1052 1414,1050 Z"/>
      <text class="contact-text" x="1490" y="1077">705-555-0148</text>
    </g>
    <g class="contact-email">
      <circle class="contact-ring" cx="1415" cy="1167" r="46"/>
      <rect class="contact-icon" x="1395" y="1153" width="42" height="28" rx="2"/>
      <path d="M1397,1155 L1416,1170 L1435,1155 M1397,1179 L1410,1166 M1435,1179 L1422,1166" fill="none" stroke="#f8f8f8" stroke-width="2.5"/>
      <text class="contact-text" x="1490" y="1180">info@phoc.ca</text>
    </g>
    <g class="contact-web">
      <circle class="contact-ring" cx="1415" cy="1273" r="46"/>
      <path class="contact-icon" d="M1406,1252 L1432,1276 L1420,1278 L1427,1292 L1421,1294 L1414,1281 L1406,1289 Z"/>
      <text class="contact-text" x="1490" y="1280">www.phoc.ca.</text>
    </g>
    <g class="contact-address">
      <circle class="contact-ring" cx="1415" cy="1380" r="46"/>
      <path class="contact-icon" fill-rule="evenodd" d="M1416,1398 L1402,1378 Q1398,1370 1401,1364 Q1406,1356 1416,1356 Q1426,1356 1431,1364 Q1434,1370 1430,1378 Z M1416,1364 A7,7 0 1 0 1416.01,1364 Z"/>
      <text class="contact-text" x="1490" y="1373">3817 Tarrow St,</text>
      <text class="contact-text" x="1490" y="1420">Ellwick Harbour</text>
    </g>
  </g>
</svg>
</body>
</html>
```